Chocolate company needing sticker for products

I have a small chocolate company Brook Lane Sweets in Austin Texas. I make all vegan, gluten free, organic, faire trade chocolate that tastes amazing! It is allergy friendly approvable by all ages. I want to have a great sticker that i can put on our boxes and bags. I am using a lot of natural craft color and brown. I am open to color options possibly for different flavors. I want the packaging to reflect the basis of my company. It is all handmade by me but i don't want it to have to much of a crafty look to it. I have attached the logo designs I have. it the sticker can have som of the bullet points about the company that would be great. But it needs to say Locally Made in Austin Texas. it also has to have the company address.
417 West Harlow Pine Rd #238 Austin Tx 78719. These things are required by the state for food regulations. I want something that looks great and I can be really proud to put on my product! Thanks so much for all of your help in advance. Dee

I also need some other information added to the sticker. Website which is brooklanesweetsqvz.com 

Phone number 512.555.0187. Instagram brooklanesweets. Thanks for your hard work! 

Industry/Entity Type

Chocolate Company

Requirements
Must have
• The logo is added at the bottom as well as designs I like I want to have a professional look but it to be approvable by all consumers. I will gig feed back as i see what designs come through. This will probably fold out into a multi design project so i will be looking for assistance on other areas of this as well. Thanks

```html
<!DOCTYPE html>
<html lang="en">
<head>
<meta charset="utf-8">
<title>Brook Lane Sweets – 90% Cocoa Sticker</title>
<link rel="stylesheet" href="https://fonts.googleapis.com/css2?family=Noto+Serif:wdth,wght@62.5,600;62.5,700&family=Yanone+Kaffeesatz:wght@600&display=swap">
<style>
  :root {
    --mint: #d8ede9;
    --sky: #97dde3;
    --cocoa: #5a180d;
    --brick: #7c2a27;
    --aqua: #5dd0de;
  }
  * { margin: 0; padding: 0; box-sizing: border-box; }
  html, body { width: 849px; height: 1200px; overflow: hidden; background: var(--mint); }
  .sticker {
    position: relative; width: 849px; height: 1200px; background: var(--mint);
    font-family: "Noto Serif", serif; font-stretch: 62.5%; color: var(--cocoa);
  }
  .frame { position: absolute; inset: 0; }
  .brand-box {
    position: absolute; left: 222px; top: 0; width: 405px; height: 392px;
    background: var(--sky); border: 6px solid var(--cocoa); border-top: none;
    box-shadow: inset 0 0 0 4px var(--sky), inset 0 0 0 6px var(--cocoa);
  }
  .brand-rule {
    position: absolute; left: 64px; width: 262px; height: 0;
    border-top: 4px dotted var(--cocoa);
  }
  .brand-rule.top { top: 38px; }
  .brand-rule.bottom { top: 340px; }
  .brand-name {
    position: absolute; left: 0; top: 66px; width: 100%;
    font-weight: 700; font-size: 84px; line-height: 88px;
    text-align: center; text-transform: uppercase; letter-spacing: 1px;
  }
  .flavour-band {
    position: absolute; left: 225px; top: 396px; width: 396px; height: 88px;
    background: var(--brick);
    display: flex; align-items: center; justify-content: center;
    font-family: "Yanone Kaffeesatz", sans-serif; font-weight: 600;
    font-size: 48px; color: var(--aqua); letter-spacing: 1px;
  }
  .band-rule { position: absolute; left: 225px; top: 493px; width: 396px; height: 8px; background: var(--cocoa); }
  .origin-badge { position: absolute; left: 298px; top: 528px; }
  .line {
    position: absolute; left: 0; width: 849px; text-align: center;
    font-weight: 700; text-transform: uppercase; white-space: nowrap;
  }
  .origin-line { top: 836px; font-size: 31px; }
  .address-line { top: 878px; font-size: 25px; font-weight: 600; }
  .claims { position: absolute; left: 0; top: 940px; }
  .claim-list { top: 1078px; font-size: 30px; }
  .contact-line { top: 1118px; font-size: 19px; font-weight: 600; text-transform: none; letter-spacing: 0.5px; }
</style>
</head>
<body>
<main class="sticker">
  <svg class="frame" width="849" height="1200" viewBox="0 0 849 1200" aria-hidden="true">
    <g fill="var(--cocoa)">
      <rect x="18" y="18" width="204" height="8"/>
      <rect x="627" y="18" width="204" height="8"/>
      <rect x="34" y="34" width="188" height="4"/>
      <rect x="627" y="34" width="181" height="4"/>
      <rect x="18" y="18" width="8" height="1155"/>
      <rect x="823" y="18" width="8" height="1155"/>
      <rect x="34" y="34" width="4" height="1120"/>
      <rect x="808" y="34" width="4" height="1120"/>
      <rect x="34" y="1150" width="778" height="4"/>
      <rect x="18" y="1165" width="813" height="8"/>
    </g>
  </svg>

  <header class="brand-box">
    <span class="brand-rule top"></span>
    <h1 class="brand-name">Brook<br>Lane<br>Sweets</h1>
    <span class="brand-rule bottom"></span>
  </header>

  <div class="flavour-band">90% COCOA</div>
  <div class="band-rule"></div>

  <svg class="origin-badge" width="252" height="252" viewBox="0 0 252 252">
    <circle cx="126" cy="126" r="119" fill="none" stroke="var(--cocoa)" stroke-width="13"/>
    <circle cx="126" cy="126" r="101" fill="var(--cocoa)" role="img" aria-label="Outline map of the state of Texas"/>
  </svg>

  <p class="line origin-line">A product locally made in Austin Texas</p>
  <p class="line address-line">417 West Harlow Pine Rd #238 Austin Tx 78719</p>

  <svg class="claims" width="849" height="110" viewBox="0 0 849 110" aria-hidden="true">
    <g fill="none" stroke="var(--cocoa)" stroke-width="6">
      <circle cx="294" cy="55" r="50"/>
      <circle cx="439" cy="55" r="50"/>
      <circle cx="584" cy="55" r="50"/>
    </g>
    <g fill="var(--cocoa)">
      <circle cx="294" cy="55" r="38"/>
      <circle cx="439" cy="55" r="38"/>
      <circle cx="584" cy="55" r="38"/>
    </g>
  </svg>

  <p class="line claim-list">Fair trade . No gluten . Vegan</p>
  <p class="line contact-line">brooklanesweetsqvz.com &nbsp;.&nbsp; 512.555.0187 &nbsp;.&nbsp; @brooklanesweets</p>
</main>
</body>
</html>
```